Nu Upsilon civil engineering orgnization activities flyer

we need flyer design for Nu Upsilon civil engineering honor society in University of Brenmoor for science and technology. the flyer contain the schedule of the expected activity. the design should have a purple color and Nu Upsilon Key and logo (you will find them in the attached file) and the design should have something referring to civil engineering

Industry/Entity Type

Education

Colors
6b449b

Requirements
Must have
• Nu Upsilon logo, key, motto
Nice to have
• civil engineering samples, purple color

```html
<!DOCTYPE html>
<html lang="en">
<head>
<meta charset="utf-8">
<title>Nu Upsilon Activities Flyer</title>
<link rel="stylesheet" href="https://fonts.googleapis.com/css2?family=PT+Sans:wght@700&family=Tinos:ital,wght@0,400;0,700;1,400&family=Arimo&display=swap">
<style>
:root{
  --purple:#6b449b;
  --purple-dark:#4a2b73;
  --purple-deep:#3a1f5e;
  --lavender:#b9a3d6;
  --paper:#eeedeb;
  --ink:#1a1a1a;
  --white:#ffffff;
}
*{margin:0;padding:0;box-sizing:border-box}
html,body{width:848px;height:1200px;overflow:hidden;background:var(--paper)}
.flyer{position:relative;width:848px;height:1200px;background:var(--paper);font-family:"Tinos",serif;color:var(--ink)}
.hero{position:absolute;left:0;top:0;width:848px;height:470px;
  background:
    linear-gradient(180deg,rgba(120,120,120,0.55) 0%,rgba(200,200,200,0) 35%,rgba(200,200,200,0) 70%,rgba(60,50,45,0.55) 100%),
    linear-gradient(100deg,#f4f4f4 0%,#e6e6e6 28%,#c7c7c7 45%,#9d9d9d 65%,#8a8a8a 100%)}
.hero-swoosh{position:absolute;left:0;top:0}
.site-photo{position:absolute;left:598px;top:254px;width:232px;height:218px;border-radius:50%;border:5px solid var(--purple);background:radial-gradient(circle at 40% 45%,#c9ad8a 0%,#9b7f5e 45%,#3e3b44 100%)}
.masthead{position:absolute;left:318px;top:34px;display:flex;align-items:flex-start;gap:10px}
.masthead-mark{width:20px;height:20px;border-radius:50%;background:var(--white);margin-top:16px}
.masthead-name{font-family:"Tinos",serif;font-weight:700;font-size:44px;line-height:50px;color:var(--white)}
.masthead-sub{font-family:"Arimo",sans-serif;font-size:11.5px;color:var(--white);text-align:right;margin-top:2px}
.tagline{position:absolute;left:674px;top:36px;font-family:"PT Sans",sans-serif;font-weight:700;font-size:21px;line-height:21px;color:var(--purple)}
.motto{position:absolute;left:12px;top:486px;width:824px;text-align:center;font-style:italic;font-size:17px;line-height:25px}
.section-title{position:absolute;left:12px;font-family:"PT Sans",sans-serif;font-weight:700;font-size:30px;color:var(--purple);line-height:32px}
.schedule{position:absolute;left:11px;top:584px;width:811px;border-collapse:collapse;font-size:15px}
.schedule th,.schedule td{border:1.5px solid var(--ink);padding:0 5px;text-align:left;font-weight:400}
.schedule th{color:var(--purple-dark);font-weight:700;height:44px;vertical-align:top;padding-top:3px;font-size:16px}
.schedule th.center{text-align:center}
.schedule td{height:23.5px}
.listing{position:absolute;left:12px;width:826px;font-size:14.5px;line-height:20.5px}
.listing b{font-weight:700}
.listing.sans{font-family:"Arimo",sans-serif;font-size:14px;line-height:24px}
.footer-contact{position:absolute;left:0;top:1094px;width:429px;height:106px;background:linear-gradient(90deg,var(--purple-deep),var(--purple));color:var(--white);padding:9px 12px;font-size:18px;line-height:23.5px}
.footer-badge{position:absolute;left:431px;top:1092px;width:100px;height:108px;background:var(--white)}
.footer-brand{position:absolute;left:545px;top:1124px;width:293px;text-align:center}
.footer-brand-row{display:flex;align-items:center;justify-content:center;gap:10px}
.footer-brand-dot{width:18px;height:18px;border-radius:50%;background:var(--purple)}
.footer-brand-name{font-family:"Tinos",serif;font-weight:700;font-size:38px;line-height:44px;color:var(--purple)}
.footer-brand-sub{font-family:"Arimo",sans-serif;font-size:9px;letter-spacing:0.5px;color:var(--purple-dark);margin-top:2px}
</style>
</head>
<body>
<main class="flyer">
  <div class="hero" role="img" aria-label="Photo of a white hard hat resting on rolled blueprints in front of a sketched perspective drawing of city buildings and palm trees"></div>
  <svg class="hero-swoosh" width="848" height="470" viewBox="0 0 848 470" aria-hidden="true">
    <path d="M0 470 L0 448 C260 440 520 420 848 350 L848 470 Z" fill="var(--paper)"/>
    <path d="M0 448 C260 440 520 420 848 350 L848 336 C520 404 260 424 0 436 Z" fill="var(--purple-dark)"/>
    <path d="M300 440 C520 422 700 390 848 360 L848 350 C700 384 520 414 300 436 Z" fill="var(--lavender)"/>
  </svg>
  <div class="site-photo" role="img" aria-label="Circular photo of students in hard hats working on a timber construction project"></div>

  <header class="masthead">
    <span class="masthead-mark"></span>
    <div>
      <div class="masthead-name">Nu Upsilon</div>
      <div class="masthead-sub">The Civil Engineering Honor Society</div>
    </div>
  </header>
  <div class="tagline">Conception<br>Design<br>Construction</div>

  <p class="motto">Nu Upsilon retains as its motto the Greek letters Nu Delta Nu, which formed the name of the junior honor society founded in 1922 at the University of Westhaven and which is one of the roots of Nu Upsilon.</p>

  <h2 class="section-title" style="top:548px">Meeting</h2>
  <table class="schedule">
    <colgroup><col style="width:137px"><col style="width:116px"><col style="width:81px"><col style="width:118px"><col style="width:191px"><col></colgroup>
    <tr><th class="center">Meeting No.</th><th>Date</th><th class="center">Time</th><th class="center">Location</th><th>Name</th><th class="center">Company</th></tr>
    <tr><td>1</td><td>9/8/2015</td><td>7 PM</td><td>BCH 124</td><td>Dr. Halvorsen</td><td></td></tr>
    <tr><td>2</td><td>9/22/2015</td><td>7 PM</td><td>BCH 124</td><td>Nolan Pryce</td><td>Brookfield Utilities</td></tr>
    <tr><td>3</td><td>10/6/2015</td><td>7 PM</td><td>BCH 124</td><td>Grant Ellery</td><td>Camp Ridgemoor</td></tr>
    <tr><td>4</td><td>10/20/2015</td><td>7 PM</td><td>BCH 124</td><td>Casey Wendell</td><td>Orbis Inc.</td></tr>
    <tr><td>5</td><td>11/3/2015</td><td>7 PM</td><td>BCH 124</td><td>Scavenger Hunt</td><td>Social</td></tr>
    <tr><td>6</td><td>11/17/2015</td><td>7 PM</td><td>BCH 124</td><td>Nomination/Owen Marlow</td><td>Harlan Finch</td></tr>
    <tr><td>7</td><td>12/1/2015</td><td>7 PM</td><td>BCH 124</td><td>Elections</td><td>-</td></tr>
  </table>

  <h2 class="section-title" style="top:796px">Service</h2>
  <div class="listing" style="top:828px">
    <p><b>Alder Creek Nature Area Service Day</b> / Saturday, Oct 24, 11 am / Alder Creek Nature Area, Brenmoor, MO 65990, United States</p>
    <p><b>Neighbors Partnership Service Day</b> / Saturday, Nov 7, 11 am / The Neighbors Resale Shop, 2400 N Crestview Ave, Brenmoor, MO 65990, United States</p>
    <p><b>Three Rivers Animal Shelter Volunteer Day</b> / Thursday, Nov 12, 12 pm / Three Rivers Animal Shelter, 812 E Maple St, Oakton, MO 65992, United States</p>
  </div>

  <h2 class="section-title" style="top:933px">Social</h2>
  <div class="listing sans" style="top:960px">
    <p>Nu Upsilon Smoker • Bowling / Starlight Lanes (1420 Queens Parkway)/ Wednesday, October 28th /9:00 PM</p>
    <p>Plaque Signing/ When: December 8th / the Commons</p>
  </div>

  <h2 class="section-title" style="top:1010px">Initiation</h2>
  <div class="listing sans" style="top:1039px">
    <p>12/12/2015&nbsp;&nbsp;&nbsp;&nbsp;&nbsp;5 PM-6PM&nbsp;&nbsp;&nbsp;&nbsp;&nbsp;BCH 314 6:30PM initiation diner / Marigold's- 1300</p>
    <p>North Lincoln Street, Oakton,</p>
  </div>

  <footer>
    <div class="footer-contact">
      University of Brenmoor PO Box 40218<br>
      Brenmoor, TX 75010-0218<br>
      555.010.0147 (PH) • 555.010.0192 (FAX)<br>
      hq@brenmoor.edu • www.nu-upsilon.org
    </div>
    <div class="footer-badge" aria-hidden="true"></div>
    <div class="footer-brand">
      <div class="footer-brand-row">
        <span class="footer-brand-dot"></span>
        <span class="footer-brand-name">Nu Upsilon</span>
      </div>
      <div class="footer-brand-sub">NATIONAL CIVIL ENGINEERING HONOR SOCIETY</div>
    </div>
  </footer>
</main>
</body>
</html>
```